Letterhead for Dorian Welk

I need a letterhead based on the business card design

Industry/Entity Type

Business

Requirements
Must have
• Footer: Dorian Welk Naturopath
Shop 4123c, 46 Carrow Lane, Sydney 2000

```html
<!DOCTYPE html>
<html lang="en">
<head>
<meta charset="utf-8">
<title>Dorian Welk Naturopath – Letterhead</title>
<link href="https://fonts.googleapis.com/css2?family=Montserrat:wght@400;500&family=Hind:wght@400;500&family=Homemade+Apple&display=swap" rel="stylesheet">
<style>
  :root {
    --backdrop: #eeeeee;
    --paper: #ffffff;
    --orange: #f0922f;
    --orange-deep: #ea7f22;
    --peach: #f8cfa4;
    --peach-soft: #fcebd9;
    --ink: #4a4a4a;
    --ink-soft: #6a6a6a;
  }
  * { box-sizing: border-box; margin: 0; padding: 0; }
  html, body {
    width: 1200px;
    height: 1000px;
    overflow: hidden;
    background: var(--backdrop);
  }
  .canvas {
    position: relative;
    width: 1200px;
    height: 1000px;
  }
  .letterhead {
    position: absolute;
    left: 275px;
    top: 40px;
    width: 650px;
    height: 920px;
    background: var(--paper);
    box-shadow: 0 6px 24px rgba(0,0,0,0.08);
    overflow: hidden;
    font-family: "Hind", sans-serif;
    color: var(--ink);
  }
  .leaf-decoration {
    position: absolute;
    left: -40px;
    top: 70px;
    width: 340px;
    height: 560px;
    border-radius: 60% 40% 55% 45% / 45% 35% 65% 55%;
    background: linear-gradient(160deg, var(--peach-soft) 0%, var(--peach) 55%, var(--peach-soft) 100%);
    opacity: 0.75;
  }
  .brand {
    position: absolute;
    right: 60px;
    top: 92px;
    display: flex;
    align-items: center;
    gap: 10px;
  }
  .brand-dot {
    width: 14px;
    height: 14px;
    border-radius: 50%;
    background: var(--orange);
  }
  .brand-name {
    font-family: "Montserrat", sans-serif;
    font-weight: 500;
    font-size: 22px;
    letter-spacing: 2px;
    text-transform: uppercase;
    color: var(--orange);
  }
  .letter-body {
    position: absolute;
    left: 62px;
    right: 62px;
    top: 190px;
    font-size: 12.5px;
    line-height: 1.6;
    color: var(--ink-soft);
  }
  .letter-body p { margin-bottom: 16px; text-align: justify; }
  .salutation { margin-bottom: 10px !important; }
  .signature {
    position: absolute;
    right: 150px;
    top: 712px;
    font-family: "Homemade Apple", cursive;
    font-size: 22px;
    color: #333333;
  }
  .footer {
    position: absolute;
    left: 0;
    right: 0;
    bottom: 36px;
    text-align: center;
  }
  .footer-name {
    font-size: 14px;
    font-weight: 500;
    color: var(--orange);
    margin-bottom: 4px;
  }
  .footer-contacts {
    display: flex;
    justify-content: center;
    align-items: center;
    gap: 14px;
    font-size: 11.5px;
    color: var(--ink);
  }
  .contact {
    display: inline-flex;
    align-items: center;
    gap: 4px;
  }
  .contact svg { width: 11px; height: 11px; fill: var(--orange); }
  .footer-band {
    position: absolute;
    left: 0;
    right: 0;
    bottom: 0;
    height: 12px;
    background: linear-gradient(90deg, var(--orange-deep), var(--orange));
  }
</style>
</head>
<body>
<main class="canvas">
  <article class="letterhead">
    <div class="leaf-decoration" role="img" aria-label="Large faint peach leaf illustration behind the letter text"></div>

    <header class="brand">
      <span class="brand-dot"></span>
      <span class="brand-name">Dorian Welk Naturopathy</span>
    </header>

    <section class="letter-body">
      <p class="salutation">Dear Client,</p>
      <p>Lorem ipsum dolor sit amet, consectetur adipiscing elit. Nulla sodales nisl vitae lorem ipsum dolor sit amet. Consectetur adipiscing elit, suspendisse feugiat eros nisl, a facilisis risus eleifend sed. Aliquam mauris enim, fermentum eu lacinia sit amet, laoreet eu leo. Nullam eleifend nulla in libero tristique cursus. Phasellus a sapien blandit, suscipit justo id, condimentum ante. Morbi tristique justo porttitor mauris pharetra, ut molestie nulla pretium. Nam pharetra velit molestie justo placerat scelerisque, et mattis dui interdum.</p>
      <p>Nulla tincidunt molestie libero vel pretium. Donec condimentum nulla sit amet risus semper imperdiet. Duis congue eros nec diam blandit, et pellentesque sapien auctor. Curabitur iaculis enim lectus, in imperdiet mauris mattis eget. Etiam ac ornare metus. Mauris risus leo, egestas at dolor a, ultrices feugiat est. Nunc faucibus scelerisque mollis. Pellentesque aliquet mauris tellus, id dignissim risus viverra et. Mauris venenatis lobortis eros.</p>
      <p>Nullam auctor venenatis metus, eu pulvinar sapien dapibus non. Cum sociis natoque penatibus et magnis dis parturient montes, nascetur ridiculus mus. Praesent sed lorem eget tortor volutpat dictum vel vel ipsum. Morbi ac mauris sed elit dictum volutpat.</p>
      <p>Best regards,</p>
    </section>

    <div class="signature">Dorian Welk</div>

    <footer class="footer">
      <p class="footer-name">Dorian Welk Naturopath</p>
      <div class="footer-contacts">
        <span class="contact">
          <svg viewBox="0 0 24 24" aria-hidden="true"><path d="M12 2a7 7 0 0 0-7 7c0 5 7 13 7 13s7-8 7-13a7 7 0 0 0-7-7zm0 9.5A2.5 2.5 0 1 1 12 6.5a2.5 2.5 0 0 1 0 5z"/></svg>
          Shop 4123c, 46 Carrow Lane, Sydney 2000
        </span>
        <span class="contact">
          <svg viewBox="0 0 24 24" aria-hidden="true"><path d="M12 2a10 10 0 1 0 0 20 10 10 0 0 0 0-20zm6.9 6h-2.9a15 15 0 0 0-1.4-3.6A8 8 0 0 1 18.9 8zM12 4c.8 1.2 1.5 2.5 1.9 4h-3.8c.4-1.5 1.1-2.8 1.9-4zM4.3 14a8 8 0 0 1 0-4h3.4a16 16 0 0 0 0 4H4.3zm.8 2h2.9c.3 1.3.8 2.5 1.4 3.6A8 8 0 0 1 5.1 16zM8 8H5.1a8 8 0 0 1 4.3-3.6C8.8 5.5 8.3 6.7 8 8zm4 12c-.8-1.2-1.5-2.5-1.9-4h3.8c-.4 1.5-1.1 2.8-1.9 4zm2.3-6H9.7a14 14 0 0 1 0-4h4.6a14 14 0 0 1 0 4zm.3 5.6c.6-1.1 1.1-2.3 1.4-3.6h2.9a8 8 0 0 1-4.3 3.6zm1.7-5.6a16 16 0 0 0 0-4h3.4a8 8 0 0 1 0 4h-3.4z"/></svg>
          dorianwelk.com.au
        </span>
        <span class="contact">
          <svg viewBox="0 0 24 24" aria-hidden="true"><circle cx="12" cy="12" r="10"/></svg>
          welkessences
        </span>
      </div>
    </footer>

    <div class="footer-band"></div>
  </article>
</main>
</body>
</html>
```